Stroke Nine Indoor Rowing Center Website

We need a very clean, professional and appealing website for a new company based in Avon, CT (USA) called "Stroke Nine Indoor Rowing Center." Basically, this company as implied by its name is an indoor rowing center that consists of indoor rowing machines (Vantor 7 ergometers, http://www.vantor7.example) and a rowing simulator (called a "glidevator", (http://www.oarmakerlabs.example). These ergometers and simulators will in turn be interfaced with visualization and analysis software (www.pulsewaterly.example) to display "virtual" races and training sessions.

Ultimately, the company will also offer advanced video analysis and 1-1 coaching, but the key message here is to leverage off the company name "Stroke Nine" (which is a term for taking 10 very hard strokes during a rowing race) and the tagline that describes the company ("Indoor Rowing Center").

We have just completed a contest to establish the company's new logo (which I am attaching to this application) and we have some other photos that we think would be helpful in visually describing the company and its services (which I will also attach).

Part of what we like about he logo we selected are the color patterns (which will contrast nicely on both light and dark backgrounds) and the way the concept of a rower is built into the name. In addition, I like the way the number 10 subtly implies IO (as in "input and output" and/or binary numbers to also indicate a "technological dimension" to the company's services).

Also, one of the websites that we really like (that offers a similar progarm and service) in the New York City area is: http://www.harbin-oars.example. The site is clean, informative and easy to navigate. In terms of pages, we'd be looking for the following:

Home
Info (with sub pages for About, Code of Conduct, Experience the Difference, and Careers)
Coaches
Programs*
Blog
Contact
Donate!

*Note that the various programs will be offered and managed through a third-party tool (www.skullhubly.example) and (https://wiki.skullhubly.example/display/FAQ/FAQs#FAQs-WhatfeaturesareavailablethroughyourClubManagementservice%3F) to allow clients to register, sign an electronic waiver and pay for programs and annual memberships. An example of these links is also available at another popular rowing web page, Tidewell Sculling in Boston, MA (https://www.tidewellsculling.example/signup/) or possibly another sign up service called "ZenTrack" (https://www.zentrackhub.example/?ql=softwrfooter)

Finally, we would also like to have links in the navigation bar to connect to social networking sites like Chatterloop, WorkLattice, Quorvo+, etc.

Lastly, I realize that ArtFlock specializes in design only, but we would be interested in receiving estimates for a "turn-key" project that would include coding (or if there are specific partners your design firm works with to codify your designs).

Please let me know if you have any questions or if I can provide any additional information.

Thank you!

Dale

Target Market(s)

Please refer to the attached Powerpoint document for information about target market and the company's vision and mission.

Industry/Entity Type

Electronic

Requirements
Must have
• Clean, intuitive, highly visual and professional look and feel. A color patter and "style guide" that works effectively with the colors and design of our logo that we can build off of as we have new content.

```html
<!DOCTYPE html>
<html lang="en">
<head>
<meta charset="utf-8">
<title>Stroke Nine Indoor Rowing Center</title>
<link rel="stylesheet" href="https://fonts.googleapis.com/css2?family=Source+Sans+3:wght@300;400;600&display=swap">
<style>
:root{
  --orange:#f07122;
  --orange-dark:#d85a10;
  --orange-ring:#f7b28a;
  --text:#555;
  --text-dark:#444;
  --muted:#888;
  --panel:#efefef;
  --panel-border:#d8d8d8;
  --page:#ffffff;
  --footer:#f7f7f7;
  --bottom:#1c1c1c;
  --icon:#6a6a6a;
}
*{margin:0;padding:0;box-sizing:border-box}
html,body{width:1200px;height:919px;overflow:hidden}
body{position:relative;background:var(--page);font-family:"Source Sans 3",sans-serif;color:var(--text)}
.abs{position:absolute}

.intro-title{left:108px;top:28px;font-size:28px;font-weight:400;color:var(--orange);letter-spacing:-.3px}
.intro-text{left:110px;top:74px;width:575px;font-size:13px;line-height:20px;color:var(--text);letter-spacing:-.1px}
.learn-more{left:109px;top:169px;font-size:13px;color:var(--orange);text-decoration:none}
.video{left:715px;top:20px;width:374px;height:167px;background:linear-gradient(120deg,#b9c3c2 0%,#7fa6a8 35%,#c9c8c2 60%,#8b8a86 100%);overflow:hidden}
.video svg{position:absolute;left:162px;top:59px}

.rail{left:108px;top:295px;width:981px;border-top:1px dashed #b5b5b5}
.feature{width:124px;height:124px;border-radius:50%;background:var(--orange);border:3px solid var(--orange-ring);display:flex;align-items:center;justify-content:center;color:#fff;font-size:16px;top:233px}
.feature-shadow{width:100px;height:8px;border-radius:50%;background:radial-gradient(ellipse,rgba(0,0,0,.35),rgba(0,0,0,0) 70%);top:365px}

.panel{top:421px;height:168px;background:linear-gradient(#f3f3f3,#ebebeb);border:1px solid var(--panel-border)}
.panel-title{font-size:17px;color:var(--text-dark);font-weight:400}
.testimonials{left:108px;width:474px}
.testimonials .panel-title{position:absolute;left:20px;top:11px}
.avatar{position:absolute;left:21px;top:41px;width:83px;height:76px;border:3px solid #fff;box-shadow:0 0 2px rgba(0,0,0,.3);background:linear-gradient(#8fae6e,#b7a090)}
.quote{position:absolute;left:132px;top:39px;width:314px;height:110px;background:#fff;border:1px solid #d6d6d6;border-radius:5px;padding:9px 14px}
.quote::before{content:"";position:absolute;left:-9px;top:18px;width:14px;height:14px;background:#fff;border-left:1px solid #d6d6d6;border-bottom:1px solid #d6d6d6;transform:rotate(45deg)}
.quote h4{font-size:15px;color:var(--text-dark);font-weight:400}
.quote time{display:block;font-size:13.5px;color:var(--muted);margin-top:3px}
.quote p{font-size:13.5px;line-height:18px;margin-top:8px;color:var(--text-dark)}

.subscribe{left:615px;width:474px}
.subscribe .panel-title{position:absolute;left:18px;top:12px}
.field{position:absolute;top:55px;height:34px;background:#fff;border:1px solid #e0e0e0;font-size:13.5px;color:#aaa;padding:8px 11px}
.subscribe-note{position:absolute;left:22px;top:110px;font-size:13px;font-style:italic;line-height:16px;color:var(--text)}
.submit{position:absolute;left:331px;top:107px;width:124px;height:36px;background:linear-gradient(#f08a2a,#c8570f);border:1px solid #b24c0b;color:#fff;font-size:21px;text-align:center;line-height:33px;font-weight:300}

.footer{left:0;top:634px;width:1200px;height:233px;background:var(--footer);border-top:1px solid #cfcfcf}
.footer::before{content:"";position:absolute;left:0;top:2px;width:100%;border-top:1px solid #e2e2e2}
.footer-title{font-size:17.5px;font-weight:400;color:var(--text-dark);top:33px}
.contact-row{font-size:14px;line-height:20px;color:var(--text)}
.contact-row svg{position:absolute;left:0;top:3px}
.contact-row span{position:absolute;left:28px;top:0;white-space:nowrap}
.link-list{list-style:none;font-size:14px;line-height:20px;top:78px}
.post{font-size:14px;line-height:17px;color:var(--text)}
.thumb{position:absolute;left:0;top:0;width:55px;height:50px;border:1px solid #d6d6d6;background:#fff;padding:4px}
.thumb div{width:100%;height:100%}
.post p{position:absolute;left:67px;top:9px;width:180px}
.social{font-size:14px;color:var(--text)}
.social i{position:absolute;left:0;top:0;width:28px;height:28px;border-radius:50%;background:radial-gradient(circle at 40% 35%,#9c8a94,#6f5d67);border:2px solid #ddd}
.social span{position:absolute;left:45px;top:5px}

.bottom-bar{left:0;top:867px;width:1200px;height:52px;background:var(--bottom);color:#c8c8c8;font-size:14px;text-align:center;line-height:50px}
</style>
</head>
<body>

<h1 class="abs intro-title">Hear what coaches and athletes have to say</h1>
<p class="abs intro-text">Lorem Ipsum is simply dummy text of the printing and typesetting industry. Lorem Ipsum has been the industry's standard dummy text ever since the 1500s, when an unknown printer took a galley of type and scrambled it to make a type specimen book. It has survived not only five centuries, but also the leap into electronic typesetting,</p>
<a class="abs learn-more" href="#">Learn More...</a>
<div class="abs video" role="img" aria-label="Video still of an athlete training on an indoor rowing machine beside a rowing tank">
  <svg width="50" height="50" viewBox="0 0 50 50"><circle cx="25" cy="25" r="24" fill="rgba(40,40,40,.75)"/><path d="M19 13 L36 25 L19 37 Z" fill="#fff"/></svg>
</div>

<div class="abs rail"></div>
<div class="abs feature" style="left:143px">Product info</div>
<div class="abs feature" style="left:338px">Try StrokeSim</div>
<div class="abs feature" style="left:533px">Rowlets</div>
<div class="abs feature" style="left:728px">Rowing</div>
<div class="abs feature" style="left:922px">Training</div>
<div class="abs feature-shadow" style="left:155px"></div>
<div class="abs feature-shadow" style="left:352px"></div>
<div class="abs feature-shadow" style="left:545px"></div>
<div class="abs feature-shadow" style="left:738px"></div>
<div class="abs feature-shadow" style="left:934px"></div>

<section class="abs panel testimonials">
  <h3 class="panel-title">Client Testimonials</h3>
  <div class="avatar" role="img" aria-label="Portrait photo of a smiling client"></div>
  <div class="quote">
    <h4>Lorem Ipsum is</h4>
    <time>December 11, 2013</time>
    <p>Lorem Ipsum is simply dummy text of the printing and typesettingindu Lorem Ipsum has been</p>
  </div>
</section>

<section class="abs panel subscribe">
  <h3 class="panel-title">Get subscriber-only Stroke Nine Indoor Rowing Center</h3>
  <div class="field" style="left:18px;width:216px">Your Name</div>
  <div class="field" style="left:243px;width:213px">Your E-mail</div>
  <p class="subscribe-note">Subscribe to get the best deals,<br>updates and latest news!</p>
  <div class="submit">Submit</div>
</section>

<footer class="abs footer">
  <h3 class="abs footer-title" style="left:108px">Stroke Nine Indoor Rowing Center</h3>
  <div class="abs contact-row" style="left:108px;top:76px;width:250px;height:40px">
    <svg width="18" height="16" viewBox="0 0 18 16"><path d="M9 1 L17 8 H14 V15 H4 V8 H1 Z" fill="var(--icon)"/><rect x="7" y="10" width="4" height="5" fill="#fff"/></svg>
    <span>Lorem Ipsum is simply dummy,<br>text of the printing.</span>
  </div>
  <div class="abs contact-row" style="left:108px;top:123px;width:250px;height:20px">
    <svg width="18" height="14" viewBox="0 0 18 14"><path d="M2 4 Q9 -1 16 4 L14 6 L12 4 H6 L4 6 Z" fill="var(--icon)"/><rect x="4" y="7" width="10" height="6" rx="1" fill="var(--icon)"/></svg>
    <span>1-555-014-2290</span>
  </div>
  <div class="abs contact-row" style="left:108px;top:150px;width:250px;height:20px">
    <svg width="18" height="14" viewBox="0 0 18 14"><rect x="1" y="2" width="16" height="11" fill="var(--icon)"/><path d="M1 2 L9 8 L17 2" stroke="#fff" stroke-width="1.3" fill="none"/></svg>
    <span style="left:31px">info@strokenine.example</span>
  </div>

  <h3 class="abs footer-title" style="left:424px">Quick Links</h3>
  <ul class="abs link-list" style="left:426px"><li>Home</li><li>About Us</li><li>Careers</li><li>Coaches</li><li>Programs</li></ul>
  <ul class="abs link-list" style="left:517px"><li>Blog</li><li>Contact Us</li><li>Donate</li></ul>

  <h3 class="abs footer-title" style="left:656px">Recent Post</h3>
  <div class="abs post" style="left:661px;top:80px;width:260px;height:50px">
    <div class="thumb"><div role="img" aria-label="Thumbnail photo of a rower" style="background:linear-gradient(#6e6a5a,#8a7a66)"></div></div>
    <p>Lorem Ipsum is simply dummy text of the printing</p>
  </div>
  <div class="abs post" style="left:661px;top:149px;width:260px;height:50px">
    <div class="thumb"><div role="img" aria-label="Thumbnail photo of a coach" style="background:linear-gradient(#c9b28a,#8f8a7f)"></div></div>
    <p>Lorem Ipsum is simply dummy text of the printing.</p>
  </div>

  <h3 class="abs footer-title" style="left:972px">Follow with us</h3>
  <div class="abs social" style="left:969px;top:72px;width:130px;height:30px"><i></i><span>Chatterloop</span></div>
  <div class="abs social" style="left:969px;top:105px;width:130px;height:30px"><i></i><span>Chirplane</span></div>
  <div class="abs social" style="left:969px;top:138px;width:130px;height:30px"><i></i><span>WorkLattice</span></div>
  <div class="abs social" style="left:969px;top:171px;width:130px;height:30px"><i></i><span>Quorvo+</span></div>
</footer>

<div class="abs bottom-bar">© Copyright 2013 strokenine.example,&nbsp;&nbsp; All Rights Reserved</div>

</body>
</html>
```